Managed technology services overview

Were looking for a clean design for our services overview

I've attached our mock up, were looking for some creative ideas on how we can showcase our products and services

Please review our website for our branding, services and products. www.valorin.com.au

Target Market(s)

Small and medium businesses

```html
<!DOCTYPE html>
<html lang="en">
<head>
<meta charset="utf-8">
<title>Valorin – Managed Technology Services</title>
<link rel="stylesheet" href="https://fonts.googleapis.com/css2?family=Open+Sans:wght@700;800&display=swap">
<style>
  :root {
    --backdrop: #6d6e71;
    --green-deep: #0b8a42;
    --green-mid: #22944a;
    --green-hub: #2fac4f;
    --orange-deep: #f07a22;
    --orange-bright: #f9a61a;
    --white: #ffffff;
  }
  html, body {
    margin: 0;
    padding: 0;
    width: 1200px;
    height: 993px;
    overflow: hidden;
    background: var(--backdrop);
  }
  .services-wheel {
    display: block;
    width: 1200px;
    height: 993px;
    font-family: "Open Sans", Arial, sans-serif;
  }
  .segment-label {
    fill: var(--white);
    font-weight: 800;
    letter-spacing: 0.5px;
  }
  .segment-label--main { font-size: 34px; }
  .segment-label--sub { font-size: 30px; }
  .segment-label--hardware { font-size: 32px; }
  .hub-disc {
    fill: var(--green-hub);
    stroke: var(--white);
    stroke-width: 2.5;
  }
  .hub-name {
    fill: var(--white);
    font-size: 44px;
    font-weight: 800;
  }
  .hub-tagline {
    fill: var(--white);
    font-size: 21px;
    font-weight: 700;
  }
</style>
</head>
<body>
<svg class="services-wheel" viewBox="0 0 1200 993" xmlns="http://www.w3.org/2000/svg" aria-label="Valorin managed technology services wheel">
  <defs>
    <radialGradient id="orangeFill" gradientUnits="userSpaceOnUse" cx="584" cy="471" r="361">
      <stop offset="0.45" stop-color="var(--orange-bright)"/>
      <stop offset="0.6" stop-color="#f89a1c"/>
      <stop offset="0.61" stop-color="#f8a01b"/>
      <stop offset="1" stop-color="var(--orange-deep)"/>
    </radialGradient>
    <radialGradient id="greenFill" gradientUnits="userSpaceOnUse" cx="584" cy="471" r="361">
      <stop offset="0.45" stop-color="#269748"/>
      <stop offset="0.595" stop-color="var(--green-mid)"/>
      <stop offset="0.6" stop-color="#24994b"/>
      <stop offset="1" stop-color="var(--green-deep)"/>
    </radialGradient>

    <path id="arc298" d="M286 471 A298 298 0 0 1 882 471"/>
    <path id="arc250" d="M334 471 A250 250 0 0 1 834 471"/>
    <path id="arc296" d="M288 471 A296 296 0 0 1 880 471"/>
    <path id="arc251" d="M333 471 A251 251 0 0 1 835 471"/>
    <path id="arc276" d="M308 471 A276 276 0 0 1 860 471"/>
    <path id="arc302" d="M282 471 A302 302 0 0 1 886 471"/>
    <path id="arc256" d="M328 471 A256 256 0 0 1 840 471"/>
  </defs>

  <rect class="backdrop" width="1200" height="993" fill="var(--backdrop)"/>

  <g class="segments">
    <path class="segment segment--communications" fill="url(#greenFill)" d="M584 471 L425.7 146.5 A361 361 0 0 1 913.8 324.2 Z"/>
    <path class="segment segment--software" fill="url(#orangeFill)" d="M584 471 L913.8 324.2 A361 361 0 0 1 742.3 795.5 Z"/>
    <path class="segment segment--data" fill="url(#greenFill)" d="M584 471 L742.3 795.5 A361 361 0 0 1 259.5 629.3 Z"/>
    <path class="segment segment--hardware" fill="url(#orangeFill)" d="M584 471 L259.5 629.3 A361 361 0 0 1 425.7 146.5 Z"/>
  </g>

  <g class="labels">
    <g transform="rotate(15 584 471)">
      <text class="segment-label segment-label--main"><textPath href="#arc298" startOffset="50%" text-anchor="middle">Communications</textPath></text>
    </g>
    <g transform="rotate(17 584 471)">
      <text class="segment-label segment-label--sub"><textPath href="#arc250" startOffset="50%" text-anchor="middle">&amp; ecommerce</textPath></text>
    </g>

    <g transform="rotate(109 584 471)">
      <text class="segment-label segment-label--main"><textPath href="#arc296" startOffset="50%" text-anchor="middle">software</textPath></text>
    </g>
    <g transform="rotate(107 584 471)">
      <text class="segment-label segment-label--sub"><textPath href="#arc251" startOffset="50%" text-anchor="middle">&amp; cloud</textPath></text>
    </g>

    <g transform="rotate(199 584 471)">
      <text class="segment-label segment-label--main"><textPath href="#arc302" startOffset="50%" text-anchor="middle">Data &amp;</textPath></text>
    </g>
    <g transform="rotate(201 584 471)">
      <text class="segment-label segment-label--sub"><textPath href="#arc256" startOffset="50%" text-anchor="middle">backup</textPath></text>
    </g>

    <g transform="rotate(292 584 471)">
      <text class="segment-label segment-label--hardware"><textPath href="#arc276" startOffset="50%" text-anchor="middle">Hardware</textPath></text>
    </g>
  </g>

  <g class="hub">
    <circle class="hub-disc" cx="584" cy="471" r="162"/>
    <text class="hub-name" x="580" y="438" text-anchor="middle">Valorin</text>
    <text class="hub-tagline" x="445" y="517">MANGED TECHNOLOGIE</text>
    <text class="hub-tagline" x="508" y="548">SOLUTION</text>
  </g>
</svg>
</body>
</html>
```